Business Card Design Project

This design is a slimline business card 45mm x90mm, the card will be printed at 49mm x 94mm and cut to 45mm x90 mm, this needs to be considered in the design. The content required on the front and back of the business card is attached in a pdf; the design will be done using photo shop as we use CS6 in our business. The design needs to be developed using a CMYK colour pallet, the main colours used on our business are red, grey black and white. A snapshot of our business brochure and new website has been provided to give you an understanding on our businesses look and feel.
FRONT OF BUSINESS CARD
Director
Marcus Fenwick
Ph+61 0421780213
www.brightlanepartners.com.au
marcusfenwick@brightlanepartners.com.au
BACK OF BUSINESS CARD
SUPPORTING CLIENTS IN
Oil & Gas I Minerals & Metals I Petrochemical I Manufacturing
Building & Construction I Telecommunication I Rail I Civil I New Industries
KNOWLEDGE I EXPERTISE I EXPERIENCE I CAPACITY

```html
<!DOCTYPE html>
<html lang="en">
<head>
<meta charset="utf-8">
<title>Business Card – Back</title>
<link href="https://fonts.googleapis.com/css2?family=Source+Sans+3:ital,wght@0,400;0,700;1,600&display=swap" rel="stylesheet">
<style>
  :root {
    --page: #ffffff;
    --guide: #66cc00;
    --steel-dark: #4b4b4b;
    --steel-mid: #6b6b6b;
    --steel-light: #ffffff;
    --band: #000000;
    --heading: #474747;
    --accent: #e8000f;
    --reverse: #ffffff;
  }
  html, body {
    margin: 0;
    padding: 0;
    width: 1200px;
    height: 1000px;
    overflow: hidden;
    background: var(--page);
    font-family: "Source Sans 3", "Myriad Pro", Arial, sans-serif;
  }
  .canvas {
    position: relative;
    width: 1200px;
    height: 1000px;
  }
  .cut-label {
    position: absolute;
    left: 160px;
    top: 24px;
    margin: 0;
    font-size: 44px;
    font-weight: 400;
    line-height: 1;
    color: var(--guide);
  }
  .cut-pointer {
    position: absolute;
    left: 0;
    top: 0;
  }
  .card {
    position: absolute;
    left: 45px;
    top: 210px;
    width: 1110px;
    height: 579px;
    background: linear-gradient(180deg,
      var(--steel-mid) 0%,
      #9a9a9a 7%,
      var(--steel-light) 17%,
      #d9d9d9 24%,
      #8a8a8a 31%,
      var(--steel-dark) 38%,
      #4e4e4e 60%,
      #545454 76%);
    overflow: hidden;
  }
  .card__band {
    position: absolute;
    left: 0;
    bottom: 0;
    width: 100%;
    height: 139px;
    background: var(--band);
  }
  .card__heading {
    position: absolute;
    right: 133px;
    top: 78px;
    margin: 0;
    font-size: 45px;
    font-style: italic;
    font-weight: 600;
    letter-spacing: -0.5px;
    color: var(--heading);
    white-space: nowrap;
  }
  .sectors {
    position: absolute;
    right: 133px;
    top: 164px;
    margin: 0;
    padding: 0;
    list-style: none;
    text-align: right;
  }
  .sectors__line {
    font-size: 36px;
    font-weight: 700;
    line-height: 50px;
    letter-spacing: -0.4px;
    color: var(--accent);
    white-space: nowrap;
  }
  .values {
    position: absolute;
    left: 0;
    bottom: 0;
    width: 100%;
    height: 139px;
    margin: 0;
    display: flex;
    align-items: center;
    justify-content: center;
    padding-bottom: 20px;
    box-sizing: border-box;
    font-size: 47px;
    font-weight: 400;
    color: var(--reverse);
    white-space: nowrap;
  }
  .values__sep {
    color: var(--accent);
    margin: 0 12px;
  }
  .cut-frame {
    position: absolute;
    left: 65px;
    top: 232px;
    width: 1070px;
    height: 535px;
    border: 3px solid var(--guide);
    border-radius: 3px;
    box-sizing: border-box;
  }
</style>
</head>
<body>
  <div class="canvas">
    <p class="cut-label">CUT</p>
    <svg class="cut-pointer" width="1200" height="1000" viewBox="0 0 1200 1000" aria-hidden="true">
      <line x1="196" y1="82" x2="285" y2="211" stroke="#66cc00" stroke-width="3"/>
    </svg>

    <section class="card" aria-label="Business card back">
      <h2 class="card__heading">SUPPORTING CLIENTS IN</h2>
      <ul class="sectors">
        <li class="sectors__line">Oil &amp; Gas I Minerals &amp; Metals</li>
        <li class="sectors__line">Petrochemical I Manufacturing</li>
        <li class="sectors__line">Building &amp; Construction</li>
        <li class="sectors__line">Telecommunication</li>
        <li class="sectors__line">Rail I Civil I New Industries</li>
      </ul>
      <div class="card__band"></div>
      <p class="values">KNOWLEDGE<span class="values__sep">I</span>EXPERTISE<span class="values__sep">I</span>EXPERIENCE<span class="values__sep">I</span>CAPACITY</p>
    </section>

    <div class="cut-frame" aria-hidden="true"></div>
  </div>
</body>
</html>
```